National Virtual CPA Firm needs post card design

Virtual CPA firm called "BRELLVO" needs a 5.5” x 8.5” post card designed to market our services to middle market mid-size american businesses. We provide Full Service Payroll (includes the processing of payroll, printing of checks and direct depositing, tax filing, and tax payments), Bookkeeping (Using their native systems, or ours), Contract CFO (with expense reduction analysis), Reporting services for business directors to make informed decisions, Capital Fundraising (Advice on seeking equity to help grow your business), and Taxes (Personal (1040), Partnership (1065), Corporate (1120, 1120S (Including Consolidated Returns)), Trust (1041) and Non-Profit (990)), including all affiliated state returns. One of our major selling points is our variety of experience, and our fast turn around times on projects.
This project specifically, I would like to highlight the bookkeeping services, but still want the tax and payroll services listed on the postcard.
I have uploaded the logo design for BRELLVO and would like a postcard that compliments the logo.
Company contact info is:
Brellvo accounting services Inc
P.O. Box 4638
Great falls, MT 59172
(800) 613-2794
Www.brellvo-example.com
Target Market(s)
Small to medium size businesses
Industry/Entity Type
Accounting
Look and feel

```html
<!DOCTYPE html>
<html lang="en">
<head>
<meta charset="utf-8">
<title>Brellvo Postcard – Front and Back</title>
<link href="https://fonts.googleapis.com/css2?family=Montserrat:wght@300;400;500;600;700;800&display=swap" rel="stylesheet">
<style>
  :root {
    --yellow: #fdd121;
    --amber: #f7b51f;
    --orange: #f29a1e;
    --green: #86c043;
    --green-dark: #6fae35;
    --ink: #2c2c2c;
    --paper: #f4f4f4;
    --white: #ffffff;
  }
  * { margin: 0; padding: 0; box-sizing: border-box; }
  html, body {
    width: 953px; height: 1200px; overflow: hidden;
    background: var(--white);
    font-family: "Montserrat", sans-serif;
  }
  .postcard {
    position: absolute; left: 190px;
    width: 612px; height: 395px; overflow: hidden;
  }
  .postcard--front { top: 122px; }
  .postcard--back { top: 654px; background: var(--paper); }
  .postcard__shapes { position: absolute; inset: 0; width: 100%; height: 100%; }

  .brand-name {
    position: absolute; left: 440px; top: 28px;
    font-size: 30px; font-weight: 500; color: var(--ink);
    letter-spacing: 0.5px; line-height: 1;
  }

  /* Front */
  .intro {
    position: absolute; left: 49px; top: 74px;
    color: var(--white); font-size: 10px; font-weight: 500;
    letter-spacing: 2px; line-height: 16px; text-transform: uppercase;
  }
  .headline {
    position: absolute; left: 48px; top: 129px;
    color: var(--ink); font-size: 20px; font-weight: 800;
    letter-spacing: 5px; line-height: 32.7px; text-transform: uppercase;
  }
  .headline__light { font-weight: 300; }
  .accent-rule {
    position: absolute; left: 51px; top: 271px;
    width: 66px; height: 5px; background: var(--white);
  }
  .badge {
    position: absolute; left: 267px; top: 98px; width: 100px;
    text-align: center; color: var(--white); line-height: 1;
  }
  .badge__strong { display: block; font-size: 20px; font-weight: 700; letter-spacing: 4px; }
  .badge__light { display: block; margin-top: 4px; font-size: 12px; font-weight: 300; letter-spacing: 3px; }

  /* Contact band */
  .contact { position: absolute; color: var(--white); line-height: 1; }
  .contact__label { display: block; font-size: 7.5px; font-weight: 400; letter-spacing: 2.5px; margin-bottom: 4px; }
  .contact__value { display: block; font-weight: 600; }
  .postcard--front .contact--web { left: 51px; top: 323px; }
  .postcard--front .contact--web .contact__value { font-size: 10px; letter-spacing: 1.3px; }
  .postcard--front .contact--phone { right: 220px; top: 323px; text-align: right; }
  .postcard--front .contact--phone .contact__value { font-size: 11.5px; letter-spacing: 2.6px; }
  .postcard--back .contact--web { left: 51px; top: 325px; }
  .postcard--back .contact--web .contact__value { font-size: 8.8px; letter-spacing: 1.1px; }
  .postcard--back .contact--phone { right: 271px; top: 322px; text-align: right; }
  .postcard--back .contact--phone .contact__value { font-size: 9.5px; letter-spacing: 2.2px; }

  /* Back */
  .services-title {
    position: absolute; left: 49px; top: 93px;
    display: flex; align-items: center; gap: 15px;
  }
  .services-title__icon { width: 26px; height: 26px; }
  .services-title__text {
    font-size: 21px; font-weight: 700; color: var(--green);
    letter-spacing: 7px; line-height: 1;
  }
  .service-list {
    position: absolute; left: 48px; top: 129px; list-style: none;
  }
  .service-list__item {
    display: flex; align-items: center; gap: 11px;
    height: 19px; font-size: 9.2px; font-weight: 600;
    color: var(--ink); letter-spacing: 0.5px; text-transform: uppercase;
  }
  .service-list__chevron { width: 8px; height: 11px; flex: none; }
</style>
</head>
<body>

<section class="postcard postcard--front" aria-label="Postcard front">
  <svg class="postcard__shapes" viewBox="0 0 1113 718" preserveAspectRatio="none">
    <defs>
      <linearGradient id="frontWarm" x1="0" y1="0" x2="1" y2="0">
        <stop offset="0" stop-color="#fdd121"/>
        <stop offset="0.45" stop-color="#fcc620"/>
        <stop offset="0.75" stop-color="#f6a91f"/>
        <stop offset="1" stop-color="#f29a1e"/>
      </linearGradient>
      <linearGradient id="photoTone" x1="0" y1="0" x2="1" y2="1">
        <stop offset="0" stop-color="#f1ede6"/>
        <stop offset="0.5" stop-color="#d6cfc4"/>
        <stop offset="1" stop-color="#4a5872"/>
      </linearGradient>
    </defs>
    <rect width="1113" height="718" fill="url(#frontWarm)"/>
    <path d="M735 0 L1113 0 L1113 161 L580 161 C590 100 650 30 735 0 Z" fill="#f4f4f4"/>
    <path d="M640 0 L735 0 C650 30 590 100 580 161 L552 175 C560 95 595 35 640 0 Z" fill="var(--green)"/>
    <path role="img" aria-label="Photo of business people reviewing financial charts with a calculator and pen"
          d="M575 161 L1113 161 L1113 718 L620 718 C652 610 642 540 610 470 C578 400 560 300 575 161 Z"
          fill="url(#photoTone)"/>
    <path d="M520 718 C580 690 610 650 618 610" fill="none" stroke="#fff3c4" stroke-width="3"/>
    <circle cx="577" cy="222" r="100" fill="var(--white)"/>
    <circle cx="577" cy="222" r="88" fill="var(--green)"/>
    <path d="M0 576 L785 576 C798 576 796 588 791 598 L774 636 C769 646 764 648 752 648 L0 648 Z" fill="var(--green)"/>
    <path d="M0 578 L785 578" stroke="var(--white)" stroke-width="2" opacity="0.6"/>
  </svg>

  <div class="brand-name">BRELLVO</div>

  <p class="intro">One of our major<br>selling points is our</p>
  <h1 class="headline">Variety of<br>experience,<br>fast turn<br><span class="headline__light">around</span></h1>
  <div class="accent-rule"></div>

  <div class="badge">
    <span class="badge__strong">FAST</span>
    <span class="badge__light">TURNING</span>
  </div>

  <div class="contact contact--web">
    <span class="contact__label">Visit</span>
    <span class="contact__value">www.brellvo-example.com</span>
  </div>
  <div class="contact contact--phone">
    <span class="contact__label">Call Us</span>
    <span class="contact__value">(800) 613-2794</span>
  </div>
</section>

<section class="postcard postcard--back" aria-label="Postcard back">
  <svg class="postcard__shapes" viewBox="0 0 1113 718" preserveAspectRatio="none">
    <defs>
      <linearGradient id="backWarm" x1="0" y1="0" x2="1" y2="1">
        <stop offset="0" stop-color="#f2c514"/>
        <stop offset="0.6" stop-color="#efb31a"/>
        <stop offset="1" stop-color="#e99a1f"/>
      </linearGradient>
    </defs>
    <path d="M565 145 L1113 145 L1113 718 L622 718 C656 620 650 558 620 490 C580 400 554 300 565 145 Z" fill="url(#backWarm)"/>
    <path d="M735 0 C620 40 545 160 545 265 C545 350 572 420 600 482 C566 402 550 320 558 232 C568 120 640 40 705 0 Z" fill="var(--green)"/>
    <path d="M520 718 C585 690 615 650 622 606" fill="none" stroke="#f2b51c" stroke-width="3"/>
    <path d="M0 583 L688 583 C700 583 698 594 693 604 L680 638 C676 646 671 648 660 648 L0 648 Z" fill="var(--green)"/>
  </svg>

  <div class="brand-name">BRELLVO</div>

  <h2 class="services-title">
    <svg class="services-title__icon" viewBox="0 0 26 26" aria-hidden="true">
      <path d="M4 15 V12 A9 9 0 0 1 22 12 V15" fill="none" stroke="#3a3a3a" stroke-width="2.2"/>
      <rect x="2" y="13" width="5" height="7" rx="2" fill="#3a3a3a"/>
      <rect x="19" y="13" width="5" height="7" rx="2" fill="#3a3a3a"/>
      <path d="M21.5 20 C21.5 23 18 24 14 24" fill="none" stroke="#3a3a3a" stroke-width="1.6"/>
    </svg>
    <span class="services-title__text">SERVICES</span>
  </h2>

  <ul class="service-list">
    <li class="service-list__item"><svg class="service-list__chevron" viewBox="0 0 8 11"><path d="M1 0 L4 0 L8 5.5 L4 11 L1 11 L5 5.5 Z" fill="var(--green)"/></svg>Full service payroll</li>
    <li class="service-list__item"><svg class="service-list__chevron" viewBox="0 0 8 11"><path d="M1 0 L4 0 L8 5.5 L4 11 L1 11 L5 5.5 Z" fill="var(--green)"/></svg>Bookkeeping</li>
    <li class="service-list__item"><svg class="service-list__chevron" viewBox="0 0 8 11"><path d="M1 0 L4 0 L8 5.5 L4 11 L1 11 L5 5.5 Z" fill="var(--green)"/></svg>Contract CFO</li>
    <li class="service-list__item"><svg class="service-list__chevron" viewBox="0 0 8 11"><path d="M1 0 L4 0 L8 5.5 L4 11 L1 11 L5 5.5 Z" fill="var(--green)"/></svg>Reporting services for business</li>
    <li class="service-list__item"><svg class="service-list__chevron" viewBox="0 0 8 11"><path d="M1 0 L4 0 L8 5.5 L4 11 L1 11 L5 5.5 Z" fill="var(--green)"/></svg>Directors</li>
    <li class="service-list__item"><svg class="service-list__chevron" viewBox="0 0 8 11"><path d="M1 0 L4 0 L8 5.5 L4 11 L1 11 L5 5.5 Z" fill="var(--green)"/></svg>And taxes</li>
    <li class="service-list__item"><svg class="service-list__chevron" viewBox="0 0 8 11"><path d="M1 0 L4 0 L8 5.5 L4 11 L1 11 L5 5.5 Z" fill="var(--green)"/></svg>Corporate</li>
    <li class="service-list__item"><svg class="service-list__chevron" viewBox="0 0 8 11"><path d="M1 0 L4 0 L8 5.5 L4 11 L1 11 L5 5.5 Z" fill="var(--green)"/></svg>Including all affiliated state returns</li>
  </ul>

  <div class="contact contact--web">
    <span class="contact__label">Visit</span>
    <span class="contact__value">www.brellvo-example.com</span>
  </div>
  <div class="contact contact--phone">
    <span class="contact__label">Call Us</span>
    <span class="contact__value">(800) 613-2794</span>
  </div>
</section>

</body>
</html>
```